Marigold Covenant - lifestyle coaching for women looking for D/s dynamic

Create website design and logo based on the requirements in the creative brief file.

Executive summary:
Company Info
Marigold Covenant is a new life and intimacy coaching company founded by a life and fitness coach. The company focuses on integrating power exchange dynamics into intimate relationships, based on the founder’s personal journey.

Product
The company offers subscription-based online coaching programs with online class structure provided through a learning management system.
Customer Profile
• Target Audience: Women aged 45-55
• Customer needs: see appendix 1
• Language: English-speaking
• Economic Status: Middle to upper class
• Device Usage: Predominantly mobile (iOS and Android)

Target Market(s)

• Target Audience: Women aged 45-55 • Customer needs: see appendix 1 • Language: English-speaking • Economic Status: Middle to upper class • Device Usage: Predominantly mobile (iOS and Android)

Industry/Entity Type

Personal Development / Lifestyle Coaching

Coding

Coded - Design and coding required

Number of Pages Required

1 page

Font styles to use
Sans Serif

Requirements
Must have
• Lead capture tools, scheduling of intake calls, payment via Stripe, ready to be maintained by WIX or Wordpress
Nice to have
• Blog page

```html
<!DOCTYPE html>
<html lang="en">
<head>
<meta charset="utf-8">
<title>Marigold Covenant — Lifestyle Coaching</title>
<link href="https://fonts.googleapis.com/css2?family=Gelasio:wght@400;500&family=Poppins:wght@300;400;500;600;700&display=swap" rel="stylesheet">
<style>
:root{
  --teal:#149f97;
  --teal-bright:#12c2bc;
  --teal-deep:#0f9c94;
  --plum:#6b2752;
  --ink:#1f1f1f;
  --muted:#555;
  --line:#d9d9d9;
  --white:#fff;
  --footer-bar:#62cfca;
}
*{box-sizing:border-box;margin:0;padding:0}
html,body{width:1200px;height:3927px;overflow:hidden;background:var(--white)}
body{font-family:"Poppins",sans-serif;color:var(--ink)}
.canvas{position:relative;width:1200px;height:3927px;overflow:hidden}
.abs{position:absolute}
.serif{font-family:"Gelasio",serif;font-weight:400}
.photo{position:absolute;border-radius:18px;overflow:hidden}

/* header */
.brand{display:flex;align-items:center;gap:10px;font-weight:700;color:var(--teal);font-size:18px;line-height:18px;letter-spacing:.5px}
.brand-dot{width:30px;height:30px;border-radius:50%;background:var(--plum);flex:none}
.nav a{position:absolute;top:60px;font-size:15px;color:var(--ink);text-decoration:none}
.nav a.active::after{content:"";position:absolute;left:0;right:0;bottom:-8px;height:2px;background:var(--teal)}
.btn-consult{left:874px;top:50px;width:238px;height:42px;border-radius:21px;background:var(--plum);color:#fff;font-size:12.5px;font-weight:600;display:flex;align-items:center;justify-content:center}

/* hero */
.hero-title{left:85px;top:200px;font-size:60px;line-height:60px;color:var(--teal)}
.hero-text{left:86px;top:420px;width:470px;font-size:15px;line-height:23px;color:var(--ink)}
.pill{display:flex;align-items:center;justify-content:center;gap:10px;border-radius:20px;background:var(--teal);color:#fff;font-size:16px;font-weight:500}
.arrows{display:flex;gap:8px}
.arrow-btn{width:30px;height:30px}

/* why */
.why-title{left:613px;top:690px;font-size:46px;color:var(--teal)}
.why-text{left:613px;top:780px;width:410px;font-size:15px;line-height:23.5px}

/* benefits */
.benefits{left:0;top:1087px;width:1200px;height:473px;background:linear-gradient(90deg,#10c4be 0%,#12bfb8 70%,#10aaa3 100%)}
.benefits-title{left:88px;top:1175px;font-size:46px;line-height:55px;color:#fff}
.benefit{position:absolute;padding:70px 36px 0 36px}
.benefit h3{font-size:18px;font-weight:600;margin:16px 0 10px}
.benefit p{font-size:15px;line-height:23px}
.benefit.light{background:#fff}
.benefit.light h3{color:var(--teal)}
.benefit.light p{color:var(--teal)}
.benefit.dark h3,.benefit.dark p{color:#fff}

/* plans */
.section-title{width:1200px;left:0;text-align:center;font-size:47px;line-height:62px;color:var(--plum)}
.plan{position:absolute;top:1816px;width:322px;height:400px;border:2px solid var(--line);border-radius:22px;background:#fff;padding:24px 20px}
.plan.featured{background:linear-gradient(160deg,#10c8c2,#11aaa4);border-color:#10b8b2;color:#fff}
.plan h4{font-size:21px;font-weight:500;line-height:26px;padding-left:4px}
.plan hr{border:0;border-top:2px solid var(--line);margin:16px 0 18px}
.plan.featured hr{border-color:rgba(255,255,255,.6)}
.plan ul{list-style:none}
.plan li{display:flex;gap:12px;font-size:15px;line-height:19px;margin-bottom:20px;align-items:flex-start}
.plan li svg{flex:none;width:24px;height:24px;margin-top:-3px}
.plan .sub{position:absolute;left:12px;right:12px;bottom:32px;height:34px;border-radius:17px;background:var(--teal-deep);color:#fff;font-size:15px;font-weight:500;display:flex;align-items:center;justify-content:center}
.plan.featured .sub{background:#fff;color:var(--ink)}
.badge{position:absolute;right:12px;top:18px;height:32px;padding:0 12px 0 6px;background:#fff;border-radius:16px 0 0 16px;color:var(--plum);font-size:14px;font-weight:600;display:flex;align-items:center;gap:8px}

/* services */
.lede{left:0;width:1200px;text-align:center;font-size:15px;line-height:23px}
.service{position:absolute;top:2545px;width:324px;height:372px;border-radius:18px;background:#fff;box-shadow:0 2px 12px rgba(0,0,0,.12);overflow:hidden}
.service .pic{height:217px}
.service h5{font-size:16px;font-weight:600;margin:20px 14px 12px}
.service p{font-size:13px;line-height:21px;color:var(--muted);margin:0 14px}

/* testimonials */
.testi{position:absolute;top:3218px;width:324px;height:256px;border-radius:18px;background:#fff;box-shadow:0 4px 14px rgba(0,0,0,.12);text-align:center;padding-top:78px}
.avatar{position:absolute;top:3137px;width:116px;height:116px;border-radius:50%;background:radial-gradient(circle at 50% 45%,#b38a78 0 30%,#6b2752 31%)}
.quote{position:absolute;top:-2px;left:18px;width:32px;height:32px;border-radius:50%;background:var(--teal-bright);color:#fff;font-size:22px;font-weight:700;line-height:38px}
.testi h6{font-size:19px;font-weight:600}
.testi .role{font-size:11px;color:var(--muted);margin-top:2px}
.testi p{font-size:12.5px;line-height:18.5px;color:#333;margin:18px 20px 0}

/* footer */
.footer{left:0;top:3596px;width:1200px;height:244px;background:linear-gradient(90deg,#10c2bc,#12b4ad)}
.footer-bar{left:0;top:3840px;width:1200px;height:87px;background:var(--footer-bar);color:#fff;text-align:center;font-size:15px;line-height:26px;padding-top:10px}
.footer-bar b{font-weight:600}
.f-head{font-size:21px;color:#fff}
.f-list{list-style:none;color:#fff;font-size:13px}
.f-list li{height:26px;display:flex;gap:8px;align-items:center}
.newsletter{left:849px;top:3697px;width:263px;height:33px;border-radius:17px;background:#fff;display:flex;align-items:center;justify-content:space-between;padding-left:24px;font-size:10px;color:#888}
.newsletter span.go{height:33px;width:98px;border-radius:17px;background:var(--plum);color:#fff;display:flex;align-items:center;justify-content:center;font-size:10px}
.social{width:24px;height:24px;border-radius:50%;background:#fff;position:absolute;top:3768px}
</style>
</head>
<body>
<div class="canvas">

  <!-- header -->
  <div class="abs brand" style="left:87px;top:54px"><span class="brand-dot"></span><span>MARIGOLD<br>COVENANT</span></div>
  <nav class="nav">
    <a class="active" style="left:348px">HOME</a>
    <a style="left:419px">ABOUT US</a>
    <a style="left:520px">SERVICES</a>
    <a style="left:616px">TESTIMONIALS</a>
    <a style="left:749px">CONTACT US</a>
  </nav>
  <div class="abs btn-consult">FREE 30-MINUTE CONSULTATION</div>

  <!-- hero -->
  <h1 class="abs serif hero-title">Elevate Your Life,<br>Embrace Your<br>Potential</h1>
  <p class="abs hero-text">Lorem ipsum dolor sit amet, consectetur adipiscing elit, sed do eiusmod tempor incididunt ut labore et dolore magna aliqua.</p>
  <div class="abs pill" style="left:82px;top:528px;width:154px;height:35px;font-size:15px">Subscribe Now</div>
  <div class="photo" role="img" aria-label="Couple embracing warmly" style="left:612px;top:189px;width:237px;height:330px;background:linear-gradient(160deg,#f3ede6,#c7a58c 55%,#e9e2d8)"></div>
  <div class="photo" role="img" aria-label="Couple stretching outdoors" style="left:874px;top:131px;width:238px;height:330px;background:linear-gradient(180deg,#d6dde2,#b7c3cc 45%,#3c5a62 80%,#cfd6da)"></div>
  <div class="abs arrows" style="left:1042px;top:500px">
    <svg class="arrow-btn" viewBox="0 0 30 30"><circle cx="15" cy="15" r="14" fill="none" stroke="#333" stroke-width="1.3"/><path d="M22 15H8M12 10.5 7.5 15l4.5 4.5" fill="none" stroke="#333" stroke-width="1.3"/></svg>
    <svg class="arrow-btn" viewBox="0 0 30 30"><circle cx="15" cy="15" r="14" fill="none" stroke="#333" stroke-width="1.3"/><path d="M8 15h14M18 10.5l4.5 4.5-4.5 4.5" fill="none" stroke="#333" stroke-width="1.3"/></svg>
  </div>

  <!-- why choose us -->
  <div class="photo" role="img" aria-label="Couple shopping online with a laptop" style="left:87px;top:682px;width:457px;height:305px;background:linear-gradient(120deg,#ddd6cc,#b88f72 45%,#7c8a99 70%,#e8e6e2)"></div>
  <h2 class="abs serif why-title">Why Choose Us?</h2>
  <p class="abs why-text">The company offers subscription-based online coaching programs with online class structure provided through a learning management system. The company offers subscription-based online coaching programs.</p>
  <div class="abs pill" style="left:613px;top:933px;width:145px;height:40px">About us
    <svg width="14" height="14" viewBox="0 0 14 14"><path d="M3 11 11 3M5 3h6v6" fill="none" stroke="#fff" stroke-width="1.5"/></svg></div>

  <!-- benefits -->
  <div class="abs benefits"></div>
  <h2 class="abs serif benefits-title">Our Health<br>Coaching Benefits</h2>
  <div class="benefit light" style="left:538px;top:1087px;width:295px;height:231px">
    <svg width="62" height="50" viewBox="0 0 62 50"><circle cx="26" cy="12" r="10" fill="#149f97"/><path d="M6 44c0-13 9-20 20-20s20 7 20 20z" fill="#149f97"/><circle cx="49" cy="26" r="11" fill="#149f97"/><text x="49" y="31" font-size="14" font-weight="700" fill="#fff" text-anchor="middle" font-family="Poppins,sans-serif">?</text></svg>
    <h3>Self Doubt</h3><p>Lorem ipsum dolor sit amet consectetur adipiscing elit.</p></div>
  <div class="benefit dark" style="left:833px;top:1087px;width:300px;height:231px">
    <svg width="50" height="50" viewBox="0 0 50 50"><circle cx="30" cy="14" r="8" fill="none" stroke="#fff" stroke-width="3"/><path d="M8 44c2-14 10-20 20-18l8 4-6 14z" fill="none" stroke="#fff" stroke-width="3"/></svg>
    <h3>Griff &amp; Death</h3><p>Lorem ipsum dolor sit amet consectetur adipiscing elit.</p></div>
  <div class="photo" role="img" aria-label="Couple with bicycles on a beach" style="left:87px;top:1318px;width:465px;height:242px;border-radius:14px 0 0 0;background:linear-gradient(180deg,#c8d6de,#9fb5c0 45%,#6b8a92 65%,#d8d2c4)"></div>
  <div class="benefit dark" style="left:552px;top:1336px;width:267px;height:224px;padding-top:30px">
    <svg width="52" height="52" viewBox="0 0 52 52"><circle cx="26" cy="18" r="12" fill="none" stroke="#fff" stroke-width="3"/><circle cx="26" cy="18" r="4" fill="#fff"/><path d="M8 48V36h36v12M17 36v-6M26 36v-6M35 36v-6" fill="none" stroke="#fff" stroke-width="3"/></svg>
    <h3>Managing People</h3><p>Lorem ipsum dolor sit amet consectetur adipiscing elit.</p></div>
  <div class="benefit light" style="left:819px;top:1320px;width:294px;height:240px;border-radius:0 16px 0 0;padding-top:46px">
    <svg width="50" height="52" viewBox="0 0 50 52"><path d="M25 30 13 18a7 7 0 0 1 12-8 7 7 0 0 1 12 8z" fill="#149f97"/><path d="M4 22l14 18v10M46 22 32 40v10" fill="none" stroke="#149f97" stroke-width="4"/><path d="M25 14v10M20 19h10" stroke="#fff" stroke-width="2.5"/></svg>
    <h3>Health &amp; Wellbeing</h3><p>Lorem ipsum dolor sit amet consectetur adipiscing elit.</p></div>

  <!-- plans -->
  <h2 class="abs serif section-title" style="top:1642px">Choose The Best Plan<br>That You Want</h2>

  <div class="plan" style="left:88px">
    <h4>Standard<br>Plan</h4><hr>
    <ul>
      <li><svg viewBox="0 0 24 24"><circle cx="12" cy="12" r="12" fill="#149f97"/><path d="m6.5 12.5 3.5 3.5 7.5-8" fill="none" stroke="#fff" stroke-width="2.3"/></svg>Coaching and Training</li>
      <li><svg viewBox="0 0 24 24"><circle cx="12" cy="12" r="12" fill="#149f97"/><path d="m6.5 12.5 3.5 3.5 7.5-8" fill="none" stroke="#fff" stroke-width="2.3"/></svg>Obstacle Standing</li>
      <li><svg viewBox="0 0 24 24"><circle cx="12" cy="12" r="12" fill="#149f97"/><path d="m6.5 12.5 3.5 3.5 7.5-8" fill="none" stroke="#fff" stroke-width="2.3"/></svg>Specific Advice Situation</li>
      <li><svg viewBox="0 0 24 24"><circle cx="12" cy="12" r="12" fill="#149f97"/><path d="m6.5 12.5 3.5 3.5 7.5-8" fill="none" stroke="#fff" stroke-width="2.3"/></svg>Includes all lifestyle plans</li>
      <li><svg viewBox="0 0 24 24"><circle cx="12" cy="12" r="12" fill="#149f97"/><path d="m6.5 12.5 3.5 3.5 7.5-8" fill="none" stroke="#fff" stroke-width="2.3"/></svg>Individual Coaching With Professioner</li>
    </ul>
    <div class="sub">SUBSCRIBE NOW</div>
  </div>

  <div class="plan featured" style="left:439px">
    <h4>Personal<br>Plan</h4>
    <div class="badge"><svg width="22" height="22" viewBox="0 0 22 22"><circle cx="11" cy="11" r="10" fill="none" stroke="#6b2752" stroke-width="1.5"/><path d="m11 5 1.8 3.9 4.2.4-3.2 2.8 1 4.1L11 14l-3.8 2.2 1-4.1L5 9.3l4.2-.4z" fill="#6b2752"/></svg>MOST POPULAR</div>
    <hr>
    <ul>
      <li><svg viewBox="0 0 24 24"><circle cx="12" cy="12" r="12" fill="#fff"/><path d="m6.5 12.5 3.5 3.5 7.5-8" fill="none" stroke="#12b9b3" stroke-width="2.3"/></svg>Coaching and Training</li>
      <li><svg viewBox="0 0 24 24"><circle cx="12" cy="12" r="12" fill="#fff"/><path d="m6.5 12.5 3.5 3.5 7.5-8" fill="none" stroke="#12b9b3" stroke-width="2.3"/></svg>Obstacle Standing</li>
      <li><svg viewBox="0 0 24 24"><circle cx="12" cy="12" r="12" fill="#fff"/><path d="m6.5 12.5 3.5 3.5 7.5-8" fill="none" stroke="#12b9b3" stroke-width="2.3"/></svg>Specific Advice Situation</li>
      <li><svg viewBox="0 0 24 24"><circle cx="12" cy="12" r="12" fill="#fff"/><path d="m6.5 12.5 3.5 3.5 7.5-8" fill="none" stroke="#12b9b3" stroke-width="2.3"/></svg>Includes all lifestyle plans</li>
      <li><svg viewBox="0 0 24 24"><circle cx="12" cy="12" r="12" fill="#fff"/><path d="m6.5 12.5 3.5 3.5 7.5-8" fill="none" stroke="#12b9b3" stroke-width="2.3"/></svg>Individual Coaching With Professioner</li>
    </ul>
    <div class="sub">SUBSCRIBE NOW</div>
  </div>

  <div class="plan" style="left:788px">
    <h4>Premium<br>Plan</h4><hr>
    <ul>
      <li><svg viewBox="0 0 24 24"><circle cx="12" cy="12" r="12" fill="#149f97"/><path d="m6.5 12.5 3.5 3.5 7.5-8" fill="none" stroke="#fff" stroke-width="2.3"/></svg>Coaching and Training</li>
      <li><svg viewBox="0 0 24 24"><circle cx="12" cy="12" r="12" fill="#149f97"/><path d="m6.5 12.5 3.5 3.5 7.5-8" fill="none" stroke="#fff" stroke-width="2.3"/></svg>Obstacle Standing</li>
      <li><svg viewBox="0 0 24 24"><circle cx="12" cy="12" r="12" fill="#149f97"/><path d="m6.5 12.5 3.5 3.5 7.5-8" fill="none" stroke="#fff" stroke-width="2.3"/></svg>Specific Advice Situation</li>
      <li><svg viewBox="0 0 24 24"><circle cx="12" cy="12" r="12" fill="#149f97"/><path d="m6.5 12.5 3.5 3.5 7.5-8" fill="none" stroke="#fff" stroke-width="2.3"/></svg>Includes all Lifetyle plans</li>
      <li><svg viewBox="0 0 24 24"><circle cx="12" cy="12" r="12" fill="#149f97"/><path d="m6.5 12.5 3.5 3.5 7.5-8" fill="none" stroke="#fff" stroke-width="2.3"/></svg>Individual Coaching With Professioner</li>
    </ul>
    <div class="sub">SUBSCRIBE NOW</div>
  </div>

  <!-- services -->
  <h2 class="abs serif section-title" style="top:2296px">What sets Marigold Covenant<br>apart from competitors?</h2>
  <p class="abs lede" style="top:2443px">Sed ut perspiciatis unde omnis iste natus error sit voluptatem accusantium doloremque laudantium,<br>totam rem aperiam, eaque ipsa quae ab illo inventore veritatis et.</p>

  <div class="service" style="left:87px"><div class="pic" role="img" aria-label="Woman training with a dumbbell" style="background:linear-gradient(90deg,#7a2a86 0%,#c9cfd3 30%,#d7c1ad 55%,#2c2c2c 75%,#e2e4e6)"></div>
    <h5>SERVICE 1</h5><p>Lorem ipsum dolor sit amet, consectetur adipiscing elit, sed do eiusmod tempor incididunt ut labore et dolore magna aliqua.</p></div>
  <div class="service" style="left:438px"><div class="pic" role="img" aria-label="Nutritionist with fresh vegetables" style="background:linear-gradient(180deg,#b9c4c8 0%,#ece9e4 45%,#c9a14a 70%,#6a9a3a 90%)"></div>
    <h5>SERVICE 2</h5><p>Lorem ipsum dolor sit amet, consectetur adipiscing elit, sed do eiusmod tempor incididunt ut labore et dolore magna aliqua.</p></div>
  <div class="service" style="left:788px"><div class="pic" role="img" aria-label="Woman receiving a relaxing head massage" style="background:linear-gradient(160deg,#eef0f2 0%,#d9dde0 40%,#c7a590 60%,#3f5f8c 85%)"></div>
    <h5>SERVICE 3</h5><p>Lorem ipsum dolor sit amet, consectetur adipiscing elit, sed do eiusmod tempor incididunt ut labore et dolore magna aliqua.</p></div>

  <div class="abs arrows" style="left:565px;top:2953px">
    <svg class="arrow-btn" viewBox="0 0 30 30"><circle cx="15" cy="15" r="14" fill="none" stroke="#333" stroke-width="1.3"/><path d="M22 15H8M12 10.5 7.5 15l4.5 4.5" fill="none" stroke="#333" stroke-width="1.3"/></svg>
    <svg class="arrow-btn" viewBox="0 0 30 30"><circle cx="15" cy="15" r="14" fill="none" stroke="#333" stroke-width="1.3"/><path d="M8 15h14M18 10.5l4.5 4.5-4.5 4.5" fill="none" stroke="#333" stroke-width="1.3"/></svg>
  </div>

  <!-- testimonials -->
  <h2 class="abs serif section-title" style="top:3038px">Testimonials</h2>

  <div class="testi" style="left:87px"><span class="quote">“</span>
    <h6>Derek Holloway</h6><div class="role">(Product Manager)</div>
    <p>There are many variations of passages of Lorem Ipsum available, but the majority have suffered alteration in some form, by injected humour, or randomised words which don't look even slightly believable.</p></div>
  <div class="testi" style="left:438px"><span class="quote">“</span>
    <h6>Nina Castell</h6><div class="role">(Associate Sales Manager)</div>
    <p>There are many variations of passages of Lorem Ipsum available, but the majority have suffered alteration in some form, by injected humour, or randomised words which don't look even slightly believable.</p></div>
  <div class="testi" style="left:788px"><span class="quote">“</span>
    <h6>Jordan Reyes</h6><div class="role">(Business Women)</div>
    <p>There are many variations of passages of Lorem Ipsum available, but the majority have suffered alteration in some form, by injected humour, or randomised words which don't look even slightly believable.</p></div>
  <div class="avatar" role="img" aria-label="Portrait of client" style="left:191px"></div>
  <div class="avatar" role="img" aria-label="Portrait of client" style="left:542px"></div>
  <div class="avatar" role="img" aria-label="Portrait of client" style="left:892px"></div>

  <div class="abs arrows" style="left:565px;top:3512px">
    <svg class="arrow-btn" viewBox="0 0 30 30"><circle cx="15" cy="15" r="14" fill="none" stroke="#333" stroke-width="1.3"/><path d="M22 15H8M12 10.5 7.5 15l4.5 4.5" fill="none" stroke="#333" stroke-width="1.3"/></svg>
    <svg class="arrow-btn" viewBox="0 0 30 30"><circle cx="15" cy="15" r="14" fill="none" stroke="#333" stroke-width="1.3"/><path d="M8 15h14M18 10.5l4.5 4.5-4.5 4.5" fill="none" stroke="#333" stroke-width="1.3"/></svg>
  </div>

  <!-- footer -->
  <footer>
    <div class="abs footer"></div>
    <div class="abs brand" style="left:87px;top:3672px;color:#fff;font-size:22px;line-height:23px"><span class="brand-dot" style="background:#fff;width:44px;height:44px"></span><span>MARIGOLD<br>COVENANT</span></div>

    <div class="abs serif f-head" style="left:357px;top:3652px">Quick Links</div>
    <ul class="abs f-list" style="left:357px;top:3690px">
      <li>↗ Home</li><li>↗ About</li><li>↗ Services</li><li>↗ Contact</li><li>↗ FAQ</li>
    </ul>

    <div class="abs serif f-head" style="left:544px;top:3652px">Contact Us</div>
    <ul class="abs f-list" style="left:544px;top:3690px">
      <li><svg width="11" height="11" viewBox="0 0 12 12"><path d="M2 1h3l1 3-2 1a7 7 0 0 0 3 3l1-2 3 1v3c-6 0-10-4-10-10z" fill="#fff"/></svg>0123456789</li>
      <li><svg width="12" height="10" viewBox="0 0 12 10"><rect width="12" height="10" rx="1" fill="#fff"/><path d="m0 1 6 5 6-5" fill="none" stroke="#12b9b3" stroke-width="1.2"/></svg>hello@marigoldcovenant.com</li>
      <li><svg width="10" height="13" viewBox="0 0 10 13"><path d="M5 13S0 7.5 0 5a5 5 0 0 1 10 0c0 2.5-5 8-5 8z" fill="#fff"/><circle cx="5" cy="5" r="1.8" fill="#12b9b3"/></svg>Address wil come here</li>
    </ul>

    <div class="abs serif f-head" style="left:849px;top:3648px">Sign Up To Our Newsletter</div>
    <div class="abs newsletter">Enter your Email<span class="go">Subscribe ↗</span></div>
    <span class="social" aria-label="Social profile" style="left:859px"></span>
    <span class="social" aria-label="Social profile" style="left:911px"></span>
    <span class="social" aria-label="Social profile" style="left:965px"></span>
    <span class="social" aria-label="Social profile" style="left:1029px"></span>

    <div class="abs footer-bar">
      <b>Privacy Policy:</b> Ensure the website includes a privacy policy that complies with relevant regulations (e.g., GDPR, CCPA).<br>
      <b>Terms of Service:</b> Provide clear terms of service to inform users about their rights and responsibilities.
    </div>
  </footer>
</div>
</body>
</html>
```